Innovative Consulting Firm Needs New Business Cards and Stationary

Our Innovative Consulting Firm, Larkfield Consulting, is in need of new business cards and stationary designs. We want two-sided cards that incorporate our logo, which is attached. We are looking for something not too formal, but is professional and slick.

Card should have the following information:
Name (ex. Tom Bradley)
Title (ex. Manager)
Address (ex. 24680 Cedar Lane)
Address 2 (ex. Suite 100)
City
State
Zip Code
Mobile
Email

The card should also have our website: www.larkfieldconsulting.example

Industry/Entity Type

Management Consulting

Contact Information for Business Card

Name (ex. Tom Bradley)
Title (ex. Manager)
Address 2 (ex. Suite 100)
City
State
Zip Code
Mobile
Email

Font styles to use
Sans Serif

Requirements
Must have
• The colors on the card must match the colors in the logo. The exact color codes are attached in a pdf.
Nice to have
• The Company's Tagline is "Focused on your Future". This might be nice to incorporate, but not necessary.

```html
<!DOCTYPE html>
<html lang="en">
<head>
<meta charset="utf-8">
<title>Larkfield Consulting – Business Card</title>
<link rel="stylesheet" href="https://fonts.googleapis.com/css2?family=Arimo:wght@400;700&display=swap">
<style>
  :root {
    --bg: #ecebe8;
    --card-white: #ffffff;
    --cream: #f6edd6;
    --blue-deep: #1a5a92;
    --blue-mid: #2673ad;
    --blue-light: #4c8fc2;
    --gold: #e8b21c;
    --ink-blue: #3d6d9c;
    --ink-grey: #4a4f55;
  }
  * { box-sizing: border-box; margin: 0; padding: 0; }
  html, body { width: 1200px; height: 1023px; overflow: hidden; }
  body {
    background: var(--bg);
    font-family: "Arimo", Arial, sans-serif;
    display: flex;
    flex-direction: column;
    align-items: center;
    justify-content: center;
    gap: 48px;
  }
  .card {
    position: relative;
    width: 760px;
    height: 434px;
    border-radius: 18px;
    overflow: hidden;
    box-shadow: 0 10px 26px rgba(0,0,0,0.18);
  }
  .card svg.art { position: absolute; inset: 0; width: 100%; height: 100%; }

  /* Front */
  .card--front { background: var(--card-white); }
  .front-logo {
    position: absolute;
    left: 170px; top: 94px;
    display: flex; align-items: center; gap: 12px;
  }
  .front-logo .mark { width: 20px; height: 20px; border-radius: 50%; background: var(--gold); }
  .front-logo .name {
    font-size: 32px; font-weight: 400; color: var(--ink-blue); letter-spacing: 1px;
  }
  .person { position: absolute; left: 48px; top: 250px; }
  .person .full-name { font-size: 26px; font-weight: 700; color: var(--ink-blue); }
  .person .title { font-size: 15px; color: var(--gold); margin-top: 4px; }
  .person .rule { width: 200px; height: 1px; background: var(--gold); margin-top: 10px; opacity: .6; }
  .contacts { position: absolute; left: 48px; top: 330px; list-style: none; }
  .contacts li {
    display: flex; align-items: flex-start; gap: 12px;
    font-size: 13px; color: var(--ink-grey); line-height: 1.35; margin-bottom: 8px;
  }
  .contacts svg { width: 16px; height: 16px; flex: none; margin-top: 1px; }

  /* Back */
  .card--back { background: linear-gradient(135deg, var(--blue-deep), var(--blue-mid) 60%, var(--blue-light)); }
  .back-logo {
    position: absolute; left: 0; right: 0; top: 170px;
    display: flex; justify-content: center; align-items: center; gap: 14px;
  }
  .back-logo .mark { width: 22px; height: 22px; border-radius: 50%; background: var(--gold); }
  .back-logo .name { font-size: 44px; color: #ffffff; letter-spacing: 1.5px; }
  .website {
    position: absolute; left: 0; right: 0; bottom: 52px;
    text-align: center; font-size: 15px; color: #ffffff; letter-spacing: 2px; opacity: .92;
  }
</style>
</head>
<body>

<section class="card card--front" aria-label="Front of business card">
  <svg class="art" viewBox="0 0 760 434" aria-hidden="true">
    <rect x="430" y="0" width="90" height="70" fill="var(--cream)" opacity=".6"/>
    <rect x="520" y="30" width="80" height="80" fill="var(--cream)" opacity=".45"/>
    <rect x="380" y="60" width="60" height="55" fill="var(--cream)" opacity=".35"/>
    <path d="M600 0 Q760 20 760 0 L760 434 L470 434 Q640 260 600 0 Z" fill="var(--blue-mid)"/>
    <path d="M640 0 C700 140 620 300 500 434 L760 434 L760 0 Z" fill="var(--blue-deep)"/>
    <path d="M560 120 C590 250 520 360 420 434 L450 434 C560 350 600 250 560 120 Z" fill="var(--blue-light)" opacity=".7"/>
  </svg>

  <div class="front-logo">
    <span class="mark"></span>
    <span class="name">Larkfield Consulting</span>
  </div>

  <div class="person">
    <p class="full-name">Tom Bradley</p>
    <p class="title">Manager</p>
    <div class="rule"></div>
  </div>

  <ul class="contacts">
    <li>
      <svg viewBox="0 0 16 16"><rect width="16" height="16" rx="3" fill="var(--gold)"/><path d="M5 4 L7 6 L6 7.5 Q7.5 9.5 8.5 10 L10 9 L12 11 L10.5 12.5 Q6 11.5 3.5 5.5 Z" fill="#fff"/></svg>
      <span>88.555.01742</span>
    </li>
    <li>
      <svg viewBox="0 0 16 16"><rect x="1" y="3.5" width="14" height="9" fill="none" stroke="var(--gold)" stroke-width="1.2"/><path d="M1 3.5 L8 9 L15 3.5" fill="none" stroke="var(--gold)" stroke-width="1.2"/></svg>
      <span>info@larkfieldconsulting.example</span>
    </li>
    <li>
      <svg viewBox="0 0 16 16"><circle cx="8" cy="8" r="8" fill="var(--gold)"/><path d="M4 8.5 L8 5 L12 8.5 M5.5 8 V11.5 H10.5 V8" fill="none" stroke="#fff" stroke-width="1.3"/></svg>
      <span>24680 Cedar Lane<br>Suite 310, Brookvale, State, 73019</span>
    </li>
  </ul>
</section>

<section class="card card--back" aria-label="Back of business card">
  <svg class="art" viewBox="0 0 760 434" aria-hidden="true">
    <rect x="210" y="60" width="110" height="100" fill="#ffffff" opacity=".05"/>
    <rect x="320" y="40" width="120" height="120" fill="#ffffff" opacity=".07"/>
    <rect x="440" y="90" width="100" height="90" fill="#ffffff" opacity=".05"/>
    <rect x="120" y="110" width="90" height="80" fill="#ffffff" opacity=".04"/>
  </svg>
  <div class="back-logo">
    <span class="mark"></span>
    <span class="name">Larkfield Consulting</span>
  </div>
  <p class="website">www.larkfieldconsulting.example</p>
</section>

</body>
</html>
```